Oil and Gas Company: Letterhead Design

In short we need a professional company letterhead designed for our Oil and Gas company.

We would like to keep the design simple and professional. Letterhead to include the company logo and color scheme, front page and continuation pages.

For reference, see attached logo below with our company logo and color scheme.

Target Market(s)

Oil & Gas Market

Industry/Entity Type

Oil And Gas

Font styles to use
Sans Serif

Requirements
Must have
• Letterhead must contain a front page & continuation page.
• Must be simple and professional in design.
• Follow our logo and color scheme.
Nice to have
• I would like to have the logo embedded in the bottom right hand portion of the page to provide some depth into the letterhead.

```html
<!DOCTYPE html>
<html lang="en">
<head>
<meta charset="utf-8">
<title>Meridian Basin Energy — Letterhead</title>
<link rel="stylesheet" href="https://fonts.googleapis.com/css2?family=Montserrat:wght@500;600&family=Didact+Gothic&display=swap">
<style>
  :root {
    --backdrop: #d9dadc;
    --paper: #ffffff;
    --ink: #2a2a2a;
    --brand-blue: #1d4e94;
    --brand-red: #e0202e;
    --signature-tone: #c9d3ee;
  }
  * { box-sizing: border-box; margin: 0; padding: 0; }
  html, body { width: 1200px; height: 900px; overflow: hidden; }
  body { background: var(--backdrop); position: relative; font-family: "Didact Gothic", sans-serif; color: var(--ink); }

  .sheet {
    position: absolute; top: 89px; width: 510px; height: 722px;
    background: var(--paper);
    box-shadow: 0 2px 6px rgba(0,0,0,.18);
  }
  .sheet--front { left: 78px; }
  .sheet--continuation { left: 612px; }

  .contact {
    position: absolute; top: 34px; right: 24px;
    font-family: "Montserrat", sans-serif; font-size: 7.4px; line-height: 10px;
    text-align: right; font-weight: 500;
  }
  .contact__line--strong { font-weight: 600; }
  .contact__icon {
    display: inline-block; width: 7px; height: 7px; border-radius: 1.5px;
    vertical-align: -1px; margin-left: 2px; background: var(--brand-blue);
  }
  .contact__icon--phone { background: var(--brand-red); }

  .letter-body {
    position: absolute; top: 240px; left: 73px; width: 372px;
    font-size: 9.3px; line-height: 11.6px; text-align: justify;
  }
  .letter-body p + p { margin-top: 11.6px; }

  .signature {
    position: absolute; top: 536px; left: 67px; width: 132px; height: 26px;
    background: var(--signature-tone); border-radius: 4px;
  }
  .signer-title { position: absolute; top: 568px; left: 73px; font-size: 10px; }

  .footer-rule {
    position: absolute; left: 0; top: 703px; width: 368px; height: 2px;
    background: var(--brand-blue);
  }
  .brand {
    position: absolute; right: 24px; top: 618px;
    display: flex; flex-direction: column; align-items: flex-end;
  }
  .brand__mark { width: 14px; height: 14px; background: var(--brand-red); margin-bottom: 34px; }
  .brand__name {
    font-family: "Montserrat", sans-serif; font-weight: 500; font-size: 10.5px;
    line-height: 12px; text-align: right; color: var(--brand-blue); letter-spacing: .2px;
  }
</style>
</head>
<body>

<section class="sheet sheet--front" aria-label="Letterhead front page">
  <address class="contact">
    <div>48 Harbor Lane</div>
    <div>Westbrook, Texas 77001</div>
    <div class="contact__line--strong">555 210 48 73 <span class="contact__icon contact__icon--phone"></span></div>
    <div class="contact__line--strong">info@meridianbasin.com <span class="contact__icon"></span></div>
    <div class="contact__line--strong">www.meridianbasin.com <span class="contact__icon"></span></div>
  </address>

  <div class="letter-body">
    <p>Letterhead samples are a great way of deciding what kind of letterhead you want to design for you and your company. The internet has a ton of great letterhead samples to browse through. Whether you want something simple, with just a couple lines of text of your business information, or something decorative and stunning, with photos and logos on the top and bottom of the page, it will be easy to find what you want, because there are samples online for basically any type of letterhead you could want.</p>
    <p>Any business could easily benefit from browsing through some letterhead samples, if only to get an idea for what kind of letterhead their company might want. Letterheads are just one of the tools that a business professional could use to help increase their customer base, and to really be memorable to everyone they write a letter to. Letterhead is quite an effective tool for marketing and advertising, but because it's such a simple and well known idea, it is often unfairly overlooked. Make sure you don't make that mistake, and make some letterhead samples of your own today.</p>
    <p>Whether you want to get new customers to remember you and become part of your clientele, or you just want to send out friendly reminders to your existing clients, customizing your own letterhead samples can really help you out. Try out some letterhead samples and you will not regret it, and I'm sure you will add a new tool to your business' arsenal of networking, marketing, and advertising tools.</p>
  </div>

  <div class="signature" role="img" aria-label="Handwritten signature of Daniel Harlow"></div>
  <div class="signer-title">company director</div>

  <div class="brand">
    <div class="brand__mark"></div>
    <div class="brand__name">MERIDIAN BASIN<br>ENERGY</div>
  </div>
  <div class="footer-rule"></div>
</section>

<section class="sheet sheet--continuation" aria-label="Letterhead continuation page">
  <div class="brand">
    <div class="brand__mark"></div>
    <div class="brand__name">MERIDIAN BASIN<br>ENERGY</div>
  </div>
  <div class="footer-rule"></div>
</section>

</body>
</html>
```